Lumawerks Business Card Design

I need a business card design for a new Business, that is focused on Custom Made Designer Furniture. that is aimed at the mid to high end markets. I would like a card that would in some way portray what I do for my clients in the way we are able to make any idea a reality and also work within a set budget to meet their requirements.
I like quite contemporary colours and styling and I want the final design to communicate a Contemporary and Professional image.

Target Market(s)

mid to high end market

Industry/Entity Type

Business

Contact Information for Business Card

Lumawerks
Darren Holtzmann
18 Wexbury Rd, Kelston, Auckland, New Zealand 0712.

Requirements
Nice to have
• I would also like to utilize the spot gloss or raised print on my cards

```html
<!DOCTYPE html>
<html lang="en">
<head>
<meta charset="utf-8">
<title>Lumawerks Business Card</title>
<link rel="stylesheet" href="https://fonts.googleapis.com/css2?family=Questrial&display=swap">
<style>
  :root {
    --stage: #4c585b;
    --card-white: #ffffff;
    --brand-green: #55ff33;
    --ink-dark: #1c1c1c;
    --tagline-grey: #ececec;
  }
  html, body {
    margin: 0;
    padding: 0;
    width: 1200px;
    height: 741px;
    overflow: hidden;
    background: var(--stage);
  }
  .canvas {
    position: relative;
    width: 1200px;
    height: 741px;
  }
  .business-card {
    position: absolute;
    left: 75px;
    top: 61px;
    width: 1050px;
    height: 618px;
    display: block;
  }
  .card-text {
    font-family: "Questrial", "Century Gothic", sans-serif;
  }
  .band-white { fill: var(--card-white); }
  .band-green { fill: var(--brand-green); }
  .first-name { fill: var(--brand-green); font-size: 92px; }
  .last-name { fill: var(--card-white); font-size: 92px; }
  .company-name { fill: var(--ink-dark); font-size: 50px; letter-spacing: 0.5px; text-transform: uppercase; }
  .tagline { fill: var(--tagline-grey); font-size: 32px; font-style: italic; }
  .address { fill: var(--brand-green); font-size: 37px; }
</style>
</head>
<body>
<main class="canvas">
  <svg class="business-card" viewBox="0 0 1050 618" xmlns="http://www.w3.org/2000/svg" role="img" aria-label="Lumawerks business card">
    <rect class="band-white" x="0" y="0" width="1050" height="618"/>
    <rect class="band-green" x="0" y="176" width="1050" height="370"/>

    <text class="card-text first-name" x="15" y="176">Darren</text>
    <text class="card-text last-name" x="427" y="258">Holtzmann</text>

    <text class="card-text company-name" x="1029" y="385" text-anchor="end">Lumawerks</text>
    <text class="card-text tagline" x="1021" y="437" text-anchor="end">Custom Made Designer Furniture</text>

    <text class="card-text address" x="18" y="600">18 Wexbury Rd, Kelston, Auckland, New Zealand 0712</text>
  </svg>
</main>
</body>
</html>
```